Leading In-Home Tutoring Company Needs Web Banners

We need a suite of web banners for our re-marketing campaign. We are based in Melbourne and heading into the busiest time of the year with back to school and we would like to help guide parents to working with us via quality designed banners with the right CTAs. Banner specs as follows (W x H in pixels)
Medium Rectangle: 300 x 250
Vertical rectangle: 240 x 400
Banner: 468 x 60
Leaderboard: 728 x 90
Square: 250 x 250
Mobile leaderboard: 320 x 50
Updates

Hi designers I'm new to this and didn't realise that I had to upload all files at the beginning. I have images that can be used for this project. Just need to work out how to upload them. Added Sunday, January 22, 2017

Hi awesome designers... I've updated the brief now with new files :)

Target Market(s)

Mothers who value kids education. Our customer can be found having morning coffee with friends in her lycra as she prepares to go to the gym. Middle class, inner city and suburban Mums. Most likely on Chatterloom.

Industry/Entity Type

It Company

Font styles to use
Sans Serif

Colors
0692cd
fbed22
f47f39
ec1f27

Requirements
Must have
• Wording should include.
• What we do: 1:1, In-Home Tutoring
• Value proposition: The Best Tutor For Your Child
• Call to Action - Free Assessment > Find Out More
• Adjusted layout to suit the sizes. Use of image where possible to provide immediate graphic display of what we do
Nice to have
• Keep it simple, create an emotive connection. Kids matter to parents and they will pay for services if we can create banners that show we care and can help wtih their education.
Should not have
• Anything negative or use fear marketing

```html
<!DOCTYPE html>
<html lang="en">
<head>
<meta charset="utf-8">
<title>StudyGlow – Web Banner Suite</title>
<link rel="stylesheet" href="https://fonts.googleapis.com/css2?family=Varela+Round&display=swap">
<style>
  :root {
    --board: #2b2b2b;
    --blue: #0692cd;
    --panel-blue: #2e9ddc;
    --yellow: #fbed22;
    --orange: #f47f39;
    --red: #ec1f27;
    --red-dark: #b3141a;
    --white: #ffffff;
    --brand-ink: #2a6fa8;
    --photo-top: #c9ced6;
    --photo-mid: #7f8fa6;
    --photo-low: #3a4f7a;
  }
  * { box-sizing: border-box; margin: 0; padding: 0; }
  html, body {
    width: 1108px; height: 1200px; overflow: hidden;
    background: var(--board);
    font-family: "Varela Round", "Helvetica Neue", Arial, sans-serif;
  }
  .board {
    position: relative; width: 960px; height: 1040px;
    transform: scale(1.15417); transform-origin: 0 0;
  }
  .banner { position: absolute; overflow: hidden; background: var(--panel-blue); }
  .banner > * { position: absolute; }
  .photo {
    background: linear-gradient(160deg, var(--photo-top) 0%, var(--photo-mid) 45%, var(--photo-low) 100%);
  }
  .shapes { left: 0; top: 0; }
  .eyebrow { color: var(--white); line-height: 1; }
  .headline { color: var(--white); text-transform: uppercase; line-height: 1.05; letter-spacing: .3px; }
  .tagline { color: var(--yellow); line-height: 1; white-space: nowrap; }
  .cta {
    background: var(--red); color: var(--white); text-align: center;
    line-height: 1.15; border-bottom: 3px solid var(--red-dark);
    display: flex; flex-direction: column; justify-content: center;
  }
  .brand { color: var(--brand-ink); line-height: 1; white-space: nowrap; }
  .center { text-align: center; }

  /* Medium rectangle */
  .medium-rect { left: 160px; top: 58px; width: 340px; height: 283px; }
  /* Square */
  .square { left: 190px; top: 393px; width: 280px; height: 280px; }
  /* Vertical rectangle */
  .vertical { left: 612px; top: 273px; width: 240px; height: 400px; }
  /* Leaderboard */
  .leaderboard { left: 106px; top: 725px; width: 728px; height: 90px; }
  /* Banner */
  .strip { left: 236px; top: 840px; width: 468px; height: 60px; }
  /* Mobile leaderboard */
  .mobile { left: 310px; top: 932px; width: 320px; height: 50px; }
</style>
</head>
<body>
<main class="board">

  <!-- Medium Rectangle 300x250 -->
  <section class="banner medium-rect">
    <div class="photo" style="left:0;top:0;width:340px;height:200px" role="img" aria-label="Photo of a tutor helping a schoolboy with his writing at a desk in front of bookshelves"></div>
    <svg class="shapes" width="340" height="283" viewBox="0 0 340 283" aria-hidden="true">
      <path d="M0,132 Q150,175 340,118 L340,283 L0,283Z" fill="var(--yellow)"/>
      <path d="M0,143 Q150,186 340,130 L340,283 L0,283Z" fill="var(--panel-blue)"/>
      <path d="M135,283 Q255,255 340,218 L340,283Z" fill="var(--white)"/>
    </svg>
    <div class="eyebrow" style="left:12px;top:170px;font-size:17px">What we do:</div>
    <div class="headline" style="left:12px;top:188px;font-size:25px">1:1, In-Home<br>Tutoring</div>
    <div class="tagline" style="left:14px;top:246px;font-size:12px">The Best Tutor For Your Child</div>
    <div class="cta" style="left:204px;top:185px;width:126px;height:38px;font-size:12px"><span>Free Assessment &gt;</span><span>Find Out More</span></div>
    <div class="brand" style="left:216px;top:261px;font-size:17px">StudyGlow</div>
  </section>

  <!-- Square 250x250 -->
  <section class="banner square">
    <div class="photo" style="left:0;top:0;width:280px;height:180px" role="img" aria-label="Photo of a tutor helping a schoolboy with his writing at a desk in front of bookshelves"></div>
    <svg class="shapes" width="280" height="280" viewBox="0 0 280 280" aria-hidden="true">
      <path d="M0,146 Q120,180 280,140 L280,280 L0,280Z" fill="var(--yellow)"/>
      <path d="M0,156 Q120,190 280,150 L280,280 L0,280Z" fill="var(--panel-blue)"/>
      <path d="M112,280 Q210,255 280,222 L280,280Z" fill="var(--white)"/>
    </svg>
    <div class="eyebrow" style="left:9px;top:183px;font-size:15px">What we do:</div>
    <div class="headline" style="left:9px;top:199px;font-size:21px">1:1, In-Home<br>Tutoring</div>
    <div class="tagline" style="left:9px;top:246px;font-size:11px">The Best Tutor For Your Child</div>
    <div class="cta" style="left:161px;top:194px;width:113px;height:34px;font-size:11px"><span>Free Assessment &gt;</span><span>Find Out More</span></div>
    <div class="brand" style="left:180px;top:260px;font-size:14px">StudyGlow</div>
  </section>

  <!-- Vertical Rectangle 240x400 -->
  <section class="banner vertical">
    <div class="photo" style="left:0;top:30px;width:240px;height:200px" role="img" aria-label="Photo of a tutor helping a schoolboy with his writing at a desk in front of bookshelves"></div>
    <svg class="shapes" width="240" height="400" viewBox="0 0 240 400" aria-hidden="true">
      <path d="M0,0 L240,0 L240,42 Q120,72 0,52Z" fill="var(--yellow)"/>
      <path d="M0,0 L240,0 L240,34 Q120,64 0,46Z" fill="var(--white)"/>
      <path d="M0,210 Q120,245 240,215 L240,400 L0,400Z" fill="var(--yellow)"/>
      <path d="M0,220 Q120,255 240,226 L240,400 L0,400Z" fill="var(--panel-blue)"/>
    </svg>
    <div class="brand" style="left:62px;top:29px;font-size:17px">StudyGlow</div>
    <div class="eyebrow center" style="left:0;top:248px;width:240px;font-size:18px">What we do:</div>
    <div class="headline center" style="left:0;top:268px;width:240px;font-size:25px">1:1, In-Home<br>Tutoring</div>
    <div class="tagline center" style="left:0;top:328px;width:240px;font-size:13px">The Best Tutor For Your Child</div>
    <div class="cta" style="left:51px;top:350px;width:138px;height:40px;font-size:12px"><span>Free Assessment &gt;</span><span>Find Out More</span></div>
  </section>

  <!-- Leaderboard 728x90 -->
  <section class="banner leaderboard">
    <div class="photo" style="left:110px;top:0;width:290px;height:90px" role="img" aria-label="Photo of a tutor helping a schoolboy with his writing at a desk in front of bookshelves"></div>
    <svg class="shapes" width="728" height="90" viewBox="0 0 728 90" aria-hidden="true">
      <path d="M0,0 L127,0 Q142,45 127,90 L0,90Z" fill="var(--yellow)"/>
      <path d="M0,0 L120,0 Q135,45 120,90 L0,90Z" fill="var(--white)"/>
      <path d="M385,0 L728,0 L728,90 L385,90 Q400,45 385,0Z" fill="var(--yellow)"/>
      <path d="M393,0 L728,0 L728,90 L393,90 Q408,45 393,0Z" fill="var(--panel-blue)"/>
    </svg>
    <div class="brand" style="left:8px;top:45px;font-size:17px">StudyGlow</div>
    <div class="eyebrow center" style="left:400px;top:7px;width:190px;font-size:16px">What we do:</div>
    <div class="headline center" style="left:400px;top:22px;width:190px;font-size:23px">1:1, In-Home<br>Tutoring</div>
    <div class="tagline center" style="left:400px;top:72px;width:200px;font-size:12px">The Best Tutor For Your Child</div>
    <div class="cta" style="left:591px;top:25px;width:126px;height:38px;font-size:12px"><span>Free Assessment &gt;</span><span>Find Out More</span></div>
  </section>

  <!-- Banner 468x60 -->
  <section class="banner strip">
    <div class="photo" style="left:90px;top:0;width:125px;height:60px" role="img" aria-label="Photo of a tutor helping a schoolboy with his writing at a desk in front of bookshelves"></div>
    <svg class="shapes" width="468" height="60" viewBox="0 0 468 60" aria-hidden="true">
      <path d="M0,0 L98,0 Q108,30 98,60 L0,60Z" fill="var(--yellow)"/>
      <path d="M0,0 L93,0 Q103,30 93,60 L0,60Z" fill="var(--white)"/>
      <path d="M203,0 L468,0 L468,60 L203,60 Q213,30 203,0Z" fill="var(--yellow)"/>
      <path d="M209,0 L468,0 L468,60 L209,60 Q219,30 209,0Z" fill="var(--panel-blue)"/>
    </svg>
    <div class="brand" style="left:3px;top:31px;font-size:12px">StudyGlow</div>
    <div class="headline center" style="left:212px;top:6px;width:146px;font-size:17px">1:1, In-Home<br>Tutoring</div>
    <div class="tagline center" style="left:212px;top:45px;width:146px;font-size:9px">The Best Tutor For Your Child</div>
    <div class="cta" style="left:360px;top:13px;width:104px;height:31px;font-size:10px"><span>Free Assessment &gt;</span><span>Find Out More</span></div>
  </section>

  <!-- Mobile Leaderboard 320x50 -->
  <section class="banner mobile">
    <svg class="shapes" width="320" height="50" viewBox="0 0 320 50" aria-hidden="true">
      <path d="M0,0 L104,0 Q112,25 104,50 L0,50Z" fill="var(--yellow)"/>
      <path d="M0,0 L99,0 Q107,25 99,50 L0,50Z" fill="var(--white)"/>
    </svg>
    <div class="brand" style="left:5px;top:27px;font-size:12px">StudyGlow</div>
    <div class="headline center" style="left:106px;top:3px;width:140px;font-size:15px">1:1, In-Home<br>Tutoring</div>
    <div class="tagline center" style="left:106px;top:37px;width:140px;font-size:9px">The Best Tutor For Your Child</div>
    <div class="cta" style="left:250px;top:8px;width:64px;height:34px;font-size:10px"><span>Find Out</span><span>More</span></div>
  </section>

</main>
</body>
</html>
```